Simple proffessional BC

I have a logo which I will attach below.
I would like the logo on the front of the card with these details in point form below:
Pre and Post Natal Yoga: Pregnancy Workshops: Hypnobirthing Courses
On the back of the card my details:
Merrin Galvey
Facebook page- calmbellieswillowharbour
Mobile- 0438 512 740

I like the idea of the card being simple, possibly just the above on a plain coloured (eggshell?) card, a card that is textured.
I am open to suggestion if it appeals!
Thank you and good luck!

Target Market(s)

Pregnant women, 20's-40's

Requirements
Must have
• Simple, compliment logo.
Make logo the feature.
Should not have

• .

```html
<!DOCTYPE html>
<html lang="en">
<head>
<meta charset="utf-8">
<title>Calm Bellies – Business Card</title>
<link rel="stylesheet" href="https://fonts.googleapis.com/css2?family=Questrial&display=swap">
<style>
  :root {
    --backdrop: #e4e4e6;
    --card: #ffffff;
    --burgundy: #7e1518;
    --amber: #eea33c;
    --ghost: #eee4e5;
    --card-w: 520px;
    --card-h: 317px;
    --band-h: 30px;
  }
  * { box-sizing: border-box; margin: 0; padding: 0; }
  html, body {
    width: 1200px; height: 900px; overflow: hidden;
    background: var(--backdrop);
    font-family: "Questrial", "Century Gothic", sans-serif;
    color: var(--burgundy);
  }
  .card {
    position: absolute;
    width: var(--card-w); height: var(--card-h);
    background: var(--card);
    box-shadow: 0 6px 18px rgba(0,0,0,.12), 0 1px 3px rgba(0,0,0,.1);
    overflow: hidden;
  }
  .card--front { left: 70px; top: 120px; }
  .card--back  { left: 610px; top: 460px; }

  .band { position: absolute; height: var(--band-h); background: var(--burgundy); }
  .accent { position: absolute; height: var(--band-h); }
  .accent--rise { background: linear-gradient(90deg, rgba(238,163,60,0) 0%, rgba(238,163,60,.85) 100%); }
  .accent--fall { background: linear-gradient(90deg, rgba(238,163,60,.85) 0%, rgba(238,163,60,0) 100%); }

  /* front */
  .card--front .band--top      { top: 0; left: 228px; right: 0; }
  .card--front .accent--top    { top: 0; left: 0; width: 222px; }
  .card--front .band--bottom   { bottom: 0; left: 0; width: 318px; }
  .card--front .accent--bottom { bottom: 0; left: 324px; right: 0; }

  .brand {
    position: absolute; left: 34px; top: 96px;
    display: flex; align-items: center; gap: 18px;
  }
  .brand__dot { width: 84px; height: 84px; border-radius: 50%; background: var(--amber); flex: none; }
  .brand__name { font-size: 46px; font-weight: 400; line-height: 1; color: var(--burgundy); }
  .services {
    position: absolute; left: 262px; top: 178px;
    list-style: none; font-size: 15px; line-height: 25px;
  }
  .services li::before { content: "•"; margin-right: 8px; }

  /* back */
  .card--back .band--top      { top: 0; left: 180px; right: 0; }
  .card--back .accent--top    { top: 0; left: 0; width: 174px; }
  .card--back .band--bottom   { bottom: 0; left: 0; width: 370px; }
  .card--back .accent--bottom { bottom: 0; left: 376px; right: 0; }

  .ghost-mark {
    position: absolute; left: 320px; top: 46px;
    width: 104px; height: 104px; border-radius: 50%; background: var(--ghost);
  }
  .holder { position: absolute; left: 28px; top: 186px; font-size: 21px; }
  .contact {
    position: absolute; left: 250px; top: 162px;
    font-size: 15px; line-height: 26px;
  }
</style>
</head>
<body>
  <section class="card card--front" aria-label="Card front">
    <div class="accent accent--top accent--rise" role="img" aria-label="Amber stripe pattern"></div>
    <div class="band band--top"></div>
    <div class="brand">
      <span class="brand__dot"></span>
      <span class="brand__name">Calm Bellies</span>
    </div>
    <ul class="services">
      <li>Pre and Post Natal Yoga</li>
      <li>Pregnancy Workshops</li>
      <li>Hypnobirthing Courses</li>
    </ul>
    <div class="band band--bottom"></div>
    <div class="accent accent--bottom accent--fall" role="img" aria-label="Amber stripe pattern"></div>
  </section>

  <section class="card card--back" aria-label="Card back">
    <div class="accent accent--top accent--rise" role="img" aria-label="Amber stripe pattern"></div>
    <div class="band band--top"></div>
    <div class="ghost-mark" aria-hidden="true"></div>
    <p class="holder">Merrin Galvey</p>
    <div class="contact">
      <p>Fb- calmbellieswillowharbour</p>
      <p>Mobile- 0438 512 740</p>
    </div>
    <div class="band band--bottom"></div>
    <div class="accent accent--bottom accent--fall" role="img" aria-label="Amber stripe pattern"></div>
  </section>
</body>
</html>
```